Trendy eye catching business card for lawn mowing business

Verge Kings, a local community lawn mowing service, requires an eye catching trendy business card to drop into letterboxes.

We could simply throw something together from a Microsoft Word template, but we are wanting something more than this. Some other business’ images are attached for some inspiration.

We are requiring the card to have Verge Kings with our slogan, Call The Pembrys. In addition, provide details with that we are a local, affordable lawn mowing service, and for other gardening matters to simply just ask!
Plus the relevant contact details, phone, email, social media.

Target Market(s)

Local community members who require assistance with their garden care

Industry/Entity Type

Gardening

Contact Information for Business Card

the name VERGE KINGS is our logo
telephone logo 0438 215 967
email logo vergekings@postbox-demo.com
Instagram logo vergekings
Facebook logo vergekings.sth
Lawn Mowing Service
Local Affordable
edge trim, blow and clipping removal included.
Other gardening matters, just ask!

Font styles to use
Serif
Sans Serif
Decorative
Script

Colors
9bcb3c
ffffff

Requirements
Must have
• All the details listed in Business Card Details.
Make these words prominent:
Verge Kings
Lawn Mowing Service
Local
Affordable
Nice to have
• Our slogan ‘Call The Pembrys’ incorporated.
Different colour background for front and reverse side
Greens, white and black colours
Subtle grass blades images incorporated
Should not have
• No images of lawnmowers.
No images of men/cartoons.
No using initials for Verge Kings

```html
<!DOCTYPE html>
<html lang="en">
<head>
<meta charset="utf-8">
<title>Verge Kings – Business Card</title>
<link href="https://fonts.googleapis.com/css2?family=Roboto:wght@400;500;700;900&display=swap" rel="stylesheet">
<style>
  :root {
    --backdrop: #3b6a22;
    --lawn: #6aaa40;
    --paper: #efefef;
    --label-bg: #e9e9e9;
    --ink: #111111;
    --white: #ffffff;
  }
  html, body {
    margin: 0;
    padding: 0;
    width: 1200px;
    height: 1101px;
    overflow: hidden;
    background: var(--backdrop);
    font-family: "Roboto", Arial, sans-serif;
    color: var(--ink);
  }
  .stage { position: relative; width: 1200px; height: 1101px; }
  .card {
    position: absolute;
    top: 268px;
    width: 303px;
    height: 529px;
    box-sizing: border-box;
  }
  /* Front */
  .card--front { left: 246px; background: var(--lawn); }
  .services {
    position: absolute; left: 31px; top: 35px;
    margin: 0; padding: 0; list-style: none;
  }
  .services li {
    display: table;
    background: var(--label-bg);
    font-size: 15px;
    line-height: 19px;
    padding: 0 8px;
    margin-bottom: 6.6px;
    white-space: nowrap;
  }
  .wordmark-panel {
    position: absolute; left: 34px; top: 391px;
    width: 241px; height: 86px;
    background: var(--label-bg);
    display: flex; align-items: center; justify-content: center;
  }
  .wordmark-panel .brand-name {
    font-weight: 900; font-size: 34px; letter-spacing: -0.5px; color: var(--ink);
  }
  .slogan {
    position: absolute; left: 34px; top: 480px; width: 241px;
    margin: 0; text-align: center;
    font-weight: 700; font-size: 23px; letter-spacing: 1px;
    color: var(--label-bg); white-space: nowrap;
  }
  /* Back */
  .card--back { left: 642px; background: var(--paper); }
  .brand-block {
    position: absolute; right: 19px; top: 19px;
    display: flex; align-items: flex-start; gap: 8px;
  }
  .brand-block .brand-square { width: 14px; height: 14px; background: var(--lawn); margin-top: 8px; }
  .brand-block .brand-name {
    font-weight: 900; font-size: 38px; line-height: 40px;
    text-align: right; color: var(--ink); letter-spacing: -0.5px;
  }
  .accent-bar {
    position: absolute; left: 0; top: 245px; width: 17px; height: 262px;
    background: var(--lawn);
  }
  .person { position: absolute; left: 29px; top: 282px; }
  .person__name { margin: 0; font-size: 18px; font-weight: 700; letter-spacing: 1.6px; }
  .person__role { margin: 1px 0 0; font-size: 14px; letter-spacing: 1.6px; }
  .contact-list {
    position: absolute; left: 29px; margin: 0; padding: 0; list-style: none;
  }
  .contact-list--direct { top: 355px; }
  .contact-list--social { top: 446px; }
  .contact-list li {
    display: flex; align-items: center;
    height: 21.5px; font-size: 14.5px; white-space: nowrap;
  }
  .contact-list .icon {
    width: 15px; height: 15px; margin-right: 13px; flex: none;
    display: flex; align-items: center; justify-content: center;
  }
  .dot { width: 11px; height: 11px; border-radius: 50%; background: var(--ink); }
</style>
</head>
<body>
<main class="stage">

  <section class="card card--front" aria-label="Card front">
    <ul class="services">
      <li>Lawn Mowing Service</li>
      <li>Edge Trim</li>
      <li>Blow &amp; Clipping Removal Included.</li>
      <li>Other Gardening Matters, Just Ask!</li>
      <li>Local. Affordable.</li>
    </ul>
    <div class="wordmark-panel"><span class="brand-name">VERGE KINGS</span></div>
    <p class="slogan">CALL THE PEMBRYS</p>
  </section>

  <section class="card card--back" aria-label="Card back">
    <div class="brand-block">
      <span class="brand-square"></span>
      <span class="brand-name">VERGE<br>KINGS</span>
    </div>
    <div class="accent-bar"></div>
    <div class="person">
      <p class="person__name">MARCUS PEMBRY</p>
      <p class="person__role">DIRECTOR</p>
    </div>
    <ul class="contact-list contact-list--direct">
      <li><span class="icon"><svg width="15" height="15" viewBox="0 0 24 24"><path fill="#111" d="M6.6 10.8c1.4 2.8 3.8 5.1 6.6 6.6l2.2-2.2c.3-.3.7-.4 1-.2 1.1.4 2.3.6 3.6.6.6 0 1 .4 1 1V20c0 .6-.4 1-1 1C10.6 21 3 13.4 3 4c0-.6.4-1 1-1h3.5c.6 0 1 .4 1 1 0 1.3.2 2.5.6 3.6.1.3 0 .7-.2 1z"/></svg></span>0438 215 967</li>
      <li><span class="icon"><svg width="15" height="12" viewBox="0 0 24 18"><path fill="#111" d="M0 0h24v18H0z"/><path fill="none" stroke="#efefef" stroke-width="2" d="M1 1l11 9 11-9"/></svg></span>vergekings@postbox-demo.com</li>
      <li><span class="icon"><svg width="15" height="15" viewBox="0 0 24 24" fill="none" stroke="#111" stroke-width="2"><circle cx="12" cy="12" r="10"/><ellipse cx="12" cy="12" rx="4.5" ry="10"/><path d="M2 12h20M4 6.5h16M4 17.5h16"/></svg></span>www.vergekings.com.au</li>
    </ul>
    <ul class="contact-list contact-list--social">
      <li><span class="icon"><span class="dot"></span></span>snapfeed.com/vergekings</li>
      <li><span class="icon"><span class="dot"></span></span>palbook.me/vergekings.sth</li>
    </ul>
  </section>

</main>
</body>
</html>
```